Lomi-Seret - Promote and Support a community

Design a website for Ethiopean Community. the design should be friendly, easy to navigate and maintain the look & feel of the Ethiopian culture. a proposed logo is attached but it can be change according to your recommendations. This is a project we are doing at a discount rate as it supports a weak community.
Please visit their current website http://www.lomi-seret.example.il/index.php?lang=en

Target Market(s)

Community members, potential doners

Industry/Entity Type

community

Number of Pages Required

1 page

Font styles to use
Sans Serif

Requirements
Must have
• easy to navigate friendly interface

```html
<!DOCTYPE html>
<html lang="en">
<head>
<meta charset="utf-8">
<title>Lomi-Seret – Ethiopian Health Promotion</title>
<link href="https://fonts.googleapis.com/css2?family=Lato:ital,wght@0,400;0,700;1,700&family=Oswald:wght@500&family=Kalam&display=swap" rel="stylesheet">
<style>
:root{
  --red:#860000;
  --red-band:#820000;
  --gold:#e2c23e;
  --orange:#f8a81c;
  --green:#1d5634;
  --green-line:#2f8a5c;
  --ink:#222;
  --muted:#444;
  --white:#fff;
}
*{box-sizing:border-box;margin:0;padding:0}
html,body{width:1200px;height:2850px;overflow:hidden}
body{position:relative;font-family:'Lato',sans-serif;color:var(--ink);background:var(--white)}
.abs{position:absolute}
a{color:inherit;text-decoration:none}

/* header */
.site-header{position:absolute;left:0;top:0;width:1200px;height:142px;background:var(--white)}
.brand{position:absolute;left:166px;top:46px;display:flex;align-items:center;gap:10px}
.brand-dot{width:40px;height:40px;border-radius:50%;background:var(--red)}
.brand-name{font-size:24px;font-weight:700;color:var(--red);white-space:nowrap}
.header-phone{position:absolute;left:411px;top:30px}
.header-phone svg{position:absolute;left:0;top:0}
.header-phone .tag{position:absolute;left:49px;top:0;white-space:nowrap;font-size:14px;font-weight:700;font-style:italic;color:var(--red)}
.header-phone .num{position:absolute;left:49px;top:18px;white-space:nowrap;font-size:17px;color:var(--ink)}
.btn-outline{position:absolute;top:27px;height:43px;border:2px solid var(--red);display:flex;align-items:center;justify-content:center;font-size:16px;color:var(--ink)}
.header-rule{position:absolute;left:411px;top:98px;width:627px;height:1px;background:#d8c56a}
.main-nav a{position:absolute;top:108px;font-size:16px;color:var(--ink)}
.main-nav a.active{color:#c0202a}

/* hero */
.hero{position:absolute;left:0;top:142px;width:1200px;height:563px;background:linear-gradient(180deg,#3c3a3a 0%,#4a3842 45%,#5a3a4a 75%,#4e3840 100%)}
.hero-kicker{position:absolute;left:0;top:149px;width:1200px;text-align:center;font-family:'Oswald',sans-serif;font-size:33px;color:var(--gold)}
.hero-title{position:absolute;left:0;top:201px;width:1200px;text-align:center;font-family:'Oswald',sans-serif;font-size:42px;line-height:57px;color:var(--white)}
.hero-btn{position:absolute;left:539px;top:336px;width:122px;height:42px;background:var(--gold);display:flex;align-items:center;justify-content:center;gap:6px;font-size:16px;color:var(--ink)}

/* section heading */
.sec-title{position:absolute;left:0;width:1200px;text-align:center;font-size:35px;color:var(--red)}
.rule{position:absolute;height:2px}
.rule .g{position:absolute;left:0;top:0;width:18px;height:2px;background:var(--green-line)}
.rule .r{position:absolute;left:26px;top:0;height:2px;background:var(--red)}

/* about */
.about-text{position:absolute;left:162px;top:850px;width:444px;font-size:14px;line-height:24.3px;color:var(--muted)}
.about-text p{margin-bottom:10px}
.about-text .reg{color:var(--red);font-weight:700;font-size:15px}
.btn-red{position:absolute;background:var(--red);color:var(--white);display:flex;align-items:center;justify-content:center;gap:7px;font-size:16px}
.about-photo{position:absolute;left:622px;top:855px;width:416px;height:327px;background:linear-gradient(180deg,#8d7a5e 0%,#4a4d5e 45%,#2c3048 100%)}
.about-photo .cap{position:absolute;left:0;bottom:12px;width:100%;text-align:center;font-family:'Kalam',sans-serif;font-size:20px;line-height:27px;color:var(--gold)}

/* supporters */
.sup-card{position:absolute;width:198px;height:143px;background:var(--white);box-shadow:0 2px 12px rgba(0,0,0,.09);display:flex;align-items:center;justify-content:center}
.sup-badge{width:80px;height:56px;border-radius:6px}

/* health */
.health{position:absolute;left:162px;top:1749px;width:876px;height:454px;background:var(--white);box-shadow:0 2px 14px rgba(0,0,0,.07)}
.health-photo{position:absolute;left:0;top:0;width:439px;height:454px;background:linear-gradient(135deg,#3e3a3c 0%,#6e6a70 40%,#c9ccd2 60%,#3d6fa6 100%)}
.health h2{position:absolute;left:484px;top:99px;width:380px;font-size:35px;line-height:48px;font-weight:400;color:var(--red)}
.health p{position:absolute;left:483px;top:213px;width:370px;font-size:15px;line-height:24px;color:var(--muted)}

/* footer */
.footer-brand{position:absolute;left:164px;top:2376px;width:136px;display:flex;align-items:center;gap:8px}
.footer-brand .brand-dot{width:28px;height:28px;flex:none}
.footer-brand .brand-name{font-size:19px}
.footer-blurb{position:absolute;left:314px;top:2340px;width:270px;font-family:'Kalam',sans-serif;font-size:15.5px;line-height:27px;color:#333}
.footer-band{position:absolute;left:0;top:2469px;width:1200px;height:381px;background:var(--red-band)}
.foot-h{position:absolute;top:2520px;font-size:19px;color:var(--white)}
.foot-rule{position:absolute;top:2551px;height:2px}
.foot-rule .y1{position:absolute;left:0;width:18px;height:2px;background:var(--gold)}
.foot-rule .w1{position:absolute;left:26px;height:2px;background:var(--white)}
.quick-links{position:absolute;left:164px;top:2574px;list-style:none;font-size:14px;line-height:24.5px;color:var(--white)}
.quick-links li::before{content:"›";margin-right:10px}
.contact-item{position:absolute;left:376px;color:var(--white);font-size:14px;line-height:18px}
.contact-item .ic{position:absolute;left:0;top:-2px;width:40px;height:40px;border:1px solid rgba(255,255,255,.8);border-radius:50%;display:flex;align-items:center;justify-content:center}
.contact-item .txt{position:absolute;left:48px;top:0;white-space:nowrap}
.copyright{position:absolute;left:162px;top:2800px;font-size:14px;color:var(--white)}

/* form */
.message-box{position:absolute;left:633px;top:2328px;width:407px;height:454px;background:var(--green)}
.message-box h3{position:absolute;left:35px;top:54px;font-size:23px;font-weight:400;color:var(--white)}
.message-box .mrule{position:absolute;left:35px;top:92px;height:2px}
.field{position:absolute;left:35px;width:334px;border-bottom:1px solid rgba(255,255,255,.25);font-size:12px;color:var(--white)}
.field svg{position:absolute;left:0;top:0}
.field span{position:absolute;left:37px;top:2px}
.submit{position:absolute;left:34px;top:377px;width:138px;height:40px;background:var(--orange);color:var(--white);display:flex;align-items:center;justify-content:center;gap:6px;font-size:17px}
</style>
</head>
<body>

<header class="site-header">
  <div class="brand"><span class="brand-dot"></span><span class="brand-name">Lomi-Seret</span></div>
  <div class="header-phone">
    <svg width="36" height="36" viewBox="0 0 24 24" fill="none" stroke="#c0202a" stroke-width="1.2"><path d="M22 16.9v3a2 2 0 0 1-2.2 2 19.8 19.8 0 0 1-8.6-3.1 19.5 19.5 0 0 1-6-6A19.8 19.8 0 0 1 2.1 4.2 2 2 0 0 1 4.1 2h3a2 2 0 0 1 2 1.7c.1 1 .4 1.9.7 2.8a2 2 0 0 1-.5 2.1L8 9.9a16 16 0 0 0 6 6l1.3-1.3a2 2 0 0 1 2.1-.4c.9.3 1.8.6 2.8.7a2 2 0 0 1 1.7 2z"/><path d="M15 2a7 7 0 0 1 7 7M15 6a3 3 0 0 1 3 3"/></svg>
    <div class="tag">Lomi Health - Ethiopian Health Promotion</div>
    <div class="num">Call Us: 04-5550172</div>
  </div>
  <a class="btn-outline" style="left:826px;width:101px">Contact Us</a>
  <a class="btn-outline" style="left:937px;width:101px">Support Us</a>
  <div class="header-rule"></div>
  <nav class="main-nav">
    <a class="active" style="left:415px">Home</a>
    <a style="left:484px">About Us</a>
    <a style="left:578px">The Community</a>
    <a style="left:718px">Pograms</a>
    <a style="left:814px">News</a>
    <a style="left:881px">Advocacy</a>
    <a style="left:977px">Partners</a>
  </nav>
</header>

<section class="hero" role="img" aria-label="Crowd of women in white shawls at a market with colourful woven baskets, darkened">
  <div class="hero-kicker">Lomi-Seret (“health” In Both Amharic And Hebrew)</div>
  <h1 class="hero-title" style="font-weight:500">Is Dedicated To Improving The Health of The<br>Ethiopian Israeli Community</h1>
  <a class="hero-btn">Support Us
    <svg width="16" height="10" viewBox="0 0 16 10"><path d="M0 5h14M10 1l4 4-4 4" stroke="#222" stroke-width="1.8" fill="none"/></svg></a>
</section>

<h2 class="sec-title" style="top:777px;font-weight:400">About Lomi-Seret</h2>
<div class="rule" style="left:558px;top:826px"><span class="g"></span><span class="r" style="width:58px"></span></div>

<div class="about-text">
  <p>Aliyah (immigration) from Ethiopia to Israel and the transition to a sedentary lifestyle has resulted in the emergence of chronic diseases, in particular diabetes. While only 0.4% of the new immigrants were diagnosed with Type 2 diabetes upon arrival, by the time they had lived in Israel for ten years the figure had risen to 18% - three times as many as in the general population. The incidence of hypertension, obesity, asthma &amp; Type 1 diabetes had also increased dramatically.</p>
  <p>Lomi-Seret was founded in 1999 by Dr. Miriam Adler, Head of the Endocrinology Unit at the Carmel Grove Medical Center.</p>
  <p class="reg">Association Registered Number: 580112233</p>
</div>
<a class="btn-red" style="left:162px;top:1136px;width:134px;height:47px">Read More
  <svg width="14" height="10" viewBox="0 0 16 10"><path d="M0 5h14M10 1l4 4-4 4" stroke="#fff" stroke-width="1.8" fill="none"/></svg></a>
<div class="about-photo" role="img" aria-label="Team members standing outside the parliament building holding an award certificate">
  <div class="cap">LOMI-SERET's Team On Receiving The<br>Award In The Knesset Israel</div>
</div>

<h2 class="sec-title" style="top:1262px;font-weight:400">Our Supporters</h2>
<div class="rule" style="left:558px;top:1311px"><span class="g"></span><span class="r" style="width:58px"></span></div>

<div class="sup-card" style="left:163px;top:1343px"><div class="sup-badge" style="background:#d9dde6"></div></div>
<div class="sup-card" style="left:388px;top:1343px"><div class="sup-badge" style="background:#cfe8e2"></div></div>
<div class="sup-card" style="left:614px;top:1343px"><div class="sup-badge" style="background:#d6ecd2"></div></div>
<div class="sup-card" style="left:839px;top:1343px"><div class="sup-badge" style="background:#d3e2f0"></div></div>
<div class="sup-card" style="left:269px;top:1513px"><div class="sup-badge" style="background:#d5ecf3"></div></div>
<div class="sup-card" style="left:494px;top:1513px"><div class="sup-badge" style="background:#dedbee"></div></div>
<div class="sup-card" style="left:720px;top:1513px"><div class="sup-badge" style="background:#d6dff0"></div></div>

<section class="health">
  <div class="health-photo" role="img" aria-label="Health worker in a white coat showing dental care to a child at a community clinic"></div>
  <h2>Health &amp; the Ethiopian Israeli Community</h2>
  <div class="rule" style="left:483px;top:203px"><span class="g"></span><span class="r" style="width:58px"></span></div>
  <p>HealthLink Today the Ethiopian Israeli community numbers over 120,000 with new immigrants still continuing to arrive.</p>
  <a class="btn-red" style="left:483px;top:299px;width:135px;height:47px">Know More
    <svg width="14" height="10" viewBox="0 0 16 10"><path d="M0 5h14M10 1l4 4-4 4" stroke="#fff" stroke-width="1.8" fill="none"/></svg></a>
</section>

<footer>
  <div class="footer-brand"><span class="brand-dot"></span><span class="brand-name">Lomi-Seret</span></div>
  <p class="footer-blurb">Lomi-Seret Non-profit Organization Operates To Promote The Ethiopian Israel Communinty Healthcare, Using Donations And Govermant Funding.</p>
  <div class="footer-band"></div>

  <h4 class="foot-h" style="left:162px;font-weight:400">Quick Links</h4>
  <div class="foot-rule" style="left:162px"><span class="y1"></span><span class="w1" style="width:56px"></span></div>
  <ul class="quick-links">
    <li>Home</li><li>About Us</li><li>The Community</li><li>Programs</li><li>News</li><li>Advocacy</li><li>Partners</li><li>Contact Us</li>
  </ul>

  <h4 class="foot-h" style="left:380px;font-weight:400">Contact Details</h4>
  <div class="foot-rule" style="left:380px"><span class="y1"></span><span class="w1" style="width:56px"></span></div>
  <div class="contact-item" style="top:2587px">
    <span class="ic"><svg width="18" height="20" viewBox="0 0 24 24" fill="none" stroke="#fff" stroke-width="1.5"><path d="M12 22s7-7 7-12a7 7 0 0 0-14 0c0 5 7 12 7 12z"/><circle cx="12" cy="10" r="2.5"/></svg></span>
    <span class="txt">Tamar 12/4 POB 2210<br>Hadera, 38140</span>
  </div>
  <div class="contact-item" style="top:2653px">
    <span class="ic"><svg width="18" height="18" viewBox="0 0 24 24" fill="none" stroke="#fff" stroke-width="1.5"><path d="M22 16.9v3a2 2 0 0 1-2.2 2 19.8 19.8 0 0 1-8.6-3.1 19.5 19.5 0 0 1-6-6A19.8 19.8 0 0 1 2.1 4.2 2 2 0 0 1 4.1 2h3a2 2 0 0 1 2 1.7c.1 1 .4 1.9.7 2.8a2 2 0 0 1-.5 2.1L8 9.9a16 16 0 0 0 6 6l1.3-1.3a2 2 0 0 1 2.1-.4c.9.3 1.8.6 2.8.7a2 2 0 0 1 1.7 2z"/></svg></span>
    <span class="txt">Phone<br>04-5550172</span>
  </div>
  <div class="contact-item" style="top:2716px">
    <span class="ic"><svg width="18" height="16" viewBox="0 0 24 20" fill="none" stroke="#fff" stroke-width="1.5"><rect x="2" y="3" width="20" height="14"/><path d="M2 3l10 8 10-8"/></svg></span>
    <span class="txt">Email<br>lomiseret@example.org</span>
  </div>

  <p class="copyright">© 2021 &nbsp;Lomi-Seret. &nbsp;All Rights Reserved.</p>

  <form class="message-box">
    <h3>Leave A Message</h3>
    <div class="mrule"><span class="abs" style="left:0;width:18px;height:2px;background:var(--orange)"></span><span class="abs" style="left:26px;width:56px;height:2px;background:var(--white)"></span></div>
    <div class="field" style="top:126px;height:31px">
      <svg width="16" height="16" viewBox="0 0 24 24" fill="none" stroke="#fff" stroke-width="1.5"><circle cx="12" cy="8" r="4"/><path d="M4 21c0-4 4-6 8-6s8 2 8 6z"/></svg><span>Name</span></div>
    <div class="field" style="top:178px;height:30px">
      <svg width="17" height="14" viewBox="0 0 24 20" fill="none" stroke="#fff" stroke-width="1.5"><rect x="2" y="3" width="20" height="14"/><path d="M2 3l10 8 10-8"/></svg><span>Email</span></div>
    <div class="field" style="top:231px;height:30px">
      <svg width="16" height="16" viewBox="0 0 24 24" fill="none" stroke="#fff" stroke-width="1.5"><path d="M22 16.9v3a2 2 0 0 1-2.2 2 19.8 19.8 0 0 1-8.6-3.1 19.5 19.5 0 0 1-6-6A19.8 19.8 0 0 1 2.1 4.2 2 2 0 0 1 4.1 2h3a2 2 0 0 1 2 1.7c.1 1 .4 1.9.7 2.8a2 2 0 0 1-.5 2.1L8 9.9a16 16 0 0 0 6 6l1.3-1.3a2 2 0 0 1 2.1-.4c.9.3 1.8.6 2.8.7a2 2 0 0 1 1.7 2z"/></svg><span>Phone</span></div>
    <div class="field" style="top:284px;height:60px">
      <svg width="16" height="16" viewBox="0 0 24 24" fill="none" stroke="#fff" stroke-width="1.5"><path d="M4 4h16v12H9l-5 4z"/><path d="M8 9h8M8 12h5"/></svg><span>Please leave your message</span></div>
    <a class="submit">Submit Now
      <svg width="14" height="10" viewBox="0 0 16 10"><path d="M0 5h14M10 1l4 4-4 4" stroke="#fff" stroke-width="1.8" fill="none"/></svg></a>
  </form>
</footer>

</body>
</html>
```